Header Design

I would like a new header design for my website - www.nestmarlo.com.

I am a Realtor and the header should reflect that and complement the theme.

The attached logo needs to be included and the information that is already there. Also, the colors need to match.

Marlo Quinby
Connecting you to the Los Angeles real estate scene.

Industry/Entity Type

Realtor

```html
<!DOCTYPE html>
<html lang="en">
<head>
<meta charset="utf-8">
<title>Marlo Quinby – Los Angeles Real Estate Header</title>
<link rel="stylesheet" href="https://fonts.googleapis.com/css2?family=Tinos:wght@400;700&display=swap">
<style>
  :root {
    --sky-top: #4b3a63;
    --sky-mid: #6e4f74;
    --sky-haze: #a4697a;
    --horizon-glow: #d9895e;
    --city-dark: #3a1f2a;
    --city-lights: #c8733f;
    --name-tint: #d9cde3;
    --mark-tint: #cfc6d8;
    --text-light: #ffffff;
  }

  * { margin: 0; padding: 0; box-sizing: border-box; }

  html, body {
    width: 1200px;
    height: 185px;
    overflow: hidden;
    background: var(--sky-top);
  }

  .site-header {
    position: relative;
    width: 1200px;
    height: 185px;
    overflow: hidden;
    font-family: "Tinos", "Times New Roman", serif;
  }

  .night-skyline {
    position: absolute;
    inset: 0;
    background:
      radial-gradient(ellipse 70% 45% at 50% 100%, rgba(232, 140, 70, 0.55), transparent 70%),
      linear-gradient(to bottom,
        var(--sky-top) 0%,
        var(--sky-mid) 45%,
        var(--sky-haze) 62%,
        var(--horizon-glow) 68%,
        var(--city-lights) 74%,
        var(--city-dark) 100%);
  }

  .brand-mark {
    position: absolute;
    left: 12px;
    top: 14px;
    display: flex;
    align-items: center;
    gap: 8px;
  }

  .brand-mark-square {
    width: 26px;
    height: 26px;
    border: 3px solid var(--mark-tint);
  }

  .brand-mark-name {
    font-size: 16px;
    font-weight: 700;
    color: var(--mark-tint);
    letter-spacing: 0.5px;
  }

  .agent-name {
    position: absolute;
    left: 410px;
    top: 16px;
    width: 300px;
    text-align: center;
    font-size: 40px;
    font-weight: 400;
    color: var(--name-tint);
    letter-spacing: 1px;
  }

  .tagline {
    position: absolute;
    left: 318px;
    top: 96px;
    font-size: 15px;
    font-weight: 700;
    color: var(--text-light);
    letter-spacing: 0.2px;
    text-transform: uppercase;
    white-space: nowrap;
  }

  .phone {
    position: absolute;
    right: 6px;
    bottom: 4px;
    font-size: 27px;
    font-weight: 400;
    color: var(--text-light);
    letter-spacing: 0.5px;
  }
</style>
</head>
<body>
  <header class="site-header">
    <div class="night-skyline" role="img" aria-label="Night view of the Los Angeles skyline and city lights under a purple dusk sky"></div>

    <div class="brand-mark">
      <span class="brand-mark-square"></span>
      <span class="brand-mark-name">Marlo Quinby</span>
    </div>

    <h1 class="agent-name">Marlo Quinby</h1>

    <p class="tagline">Connecting you to the Los Angeles real estate scene</p>

    <p class="phone">310.555.0148</p>
  </header>
</body>
</html>
```